Two (2) Merchant Advance Banner Ads

I need two (2) ads with rotating gif with 3 transitions for http://lendorbit.com/

Ad Specs:
Ad 1 must be an image equal to 250x250 pixels for website and email newsletter. .jpg, .gif, and
.png okay. No Flash!

Ad 2 must be an image equal to 720x90 pixels for website and mobile device view. .jpg, .gif, and
.png only. No Flash!

Client: Marlowe Funding Partners merchant cash advance company out of Chicago. They provide alternative (to a bank loan) financing for small business owners across the U.S.
Here's their website: www.marlowefp.com

Purpose: Recruit 3rd party sellers of alternative financing. There are many sales financing professionals already out there soliciting small businesses, we want them to make a decision to sell Marlowe's financing product to small businesses.

Copy:
Real People.
Competitive Commissions.
Great Rates.

I would like the logo (attached), phone number and CTA button to appear on all three transitions.
Call (888) 471-2859
Button: Get Started

Style:
Either something clean and simple, or something similar (not identifcal) to ads attached.
Brand standards guide is attached. Please use colors from guide.

```html
<!DOCTYPE html>
<html lang="en">
<head>
<meta charset="utf-8">
<title>Marlowe Funding Partners – Partner Banner</title>
<link rel="stylesheet" href="https://fonts.googleapis.com/css2?family=Dosis:wght@500;600&family=Open+Sans:wght@600;700&display=swap">
<style>
  :root {
    --lime: #a9bb2c;
    --lime-soft: #e3e9b8;
    --lime-pale: #f4f7e2;
    --slate: #5b6b79;
    --slate-dark: #4a5966;
    --ink: #4f5b63;
    --mist: #eef1e4;
    --white: #ffffff;
  }
  html, body {
    margin: 0;
    padding: 0;
    width: 1200px;
    height: 150px;
    overflow: hidden;
    background: var(--white);
  }
  .banner {
    position: relative;
    width: 1200px;
    height: 150px;
    overflow: hidden;
    background: linear-gradient(90deg, var(--lime-soft) 0%, var(--lime-pale) 45%, var(--white) 70%);
  }
  .swoosh {
    position: absolute;
    inset: 0;
  }
  .board {
    position: absolute;
    left: 12px;
    top: 8px;
    width: 424px;
    height: 102px;
    background: var(--white);
    border: 2px solid var(--slate);
    box-sizing: border-box;
  }
  .board-stand {
    position: absolute;
    left: 225px;
    top: 108px;
    width: 2px;
    height: 10px;
    background: var(--slate);
  }
  .board-knob {
    position: absolute;
    left: 218px;
    top: 117px;
    width: 12px;
    height: 12px;
    border: 2px solid var(--slate);
    border-radius: 50%;
    background: var(--white);
  }
  .headline {
    position: absolute;
    left: 12px;
    top: -6px;
    margin: 0;
    font-family: "Dosis", sans-serif;
    font-weight: 600;
    font-size: 62px;
    line-height: 1.1;
    color: var(--lime);
    letter-spacing: 0.5px;
  }
  .tagline {
    position: absolute;
    left: 0;
    right: 0;
    top: 64px;
    height: 34px;
    margin: 0;
    border-top: 2px solid var(--slate);
    font-family: "Open Sans", sans-serif;
    font-weight: 700;
    font-size: 15.5px;
    line-height: 34px;
    color: var(--ink);
    letter-spacing: 0.6px;
    text-transform: uppercase;
    text-align: center;
  }
  .phone {
    position: absolute;
    left: 462px;
    top: 10px;
    margin: 0;
    font-family: "Dosis", sans-serif;
    font-weight: 500;
    font-size: 58px;
    line-height: 1.1;
    color: var(--lime);
    letter-spacing: 0.5px;
  }
  .cta {
    position: absolute;
    left: 562px;
    top: 87px;
    width: 141px;
    height: 40px;
    background: var(--lime);
    color: var(--white);
    font-family: "Open Sans", sans-serif;
    font-weight: 700;
    font-size: 15px;
    line-height: 40px;
    text-align: center;
  }
  .brand {
    position: absolute;
    left: 905px;
    top: 88px;
    width: 230px;
    text-align: center;
    font-family: "Dosis", sans-serif;
    font-weight: 600;
    font-size: 24px;
    line-height: 1.05;
    color: var(--slate-dark);
  }
</style>
</head>
<body>
  <div class="banner">
    <svg class="swoosh" width="1200" height="150" viewBox="0 0 1200 150" aria-hidden="true">
      <path d="M720 150 C800 70 950 10 1200 0 L1200 150 Z" fill="var(--mist)"/>
      <path d="M745 150 C830 70 980 20 1200 12 L1200 150 Z" fill="var(--white)"/>
      <path d="M1000 0 L1200 0 L1200 10 C1120 8 1060 4 1000 0 Z" fill="var(--lime)"/>
      <path d="M742 150 C820 60 970 8 1200 4 L1200 40 C1010 46 880 90 825 150 Z" fill="var(--slate)"/>
      <path d="M1200 48 C1060 52 950 92 915 150 L1200 150 Z" fill="var(--white)"/>
    </svg>

    <div class="board">
      <h1 class="headline">Real PeoPle.</h1>
      <p class="tagline">Competitive Commissions. &nbsp;Great Rates.</p>
    </div>
    <div class="board-stand"></div>
    <div class="board-knob"></div>

    <p class="phone">(888) 471-2859</p>
    <div class="cta" role="button">Get Started</div>

    <div class="brand">Marlowe<br>Funding Partners</div>
  </div>
</body>
</html>
```